Web Design for Rubbish Removal Company

I am looking for a custom web design that is clean and modern which also has a professional trustworthy feel to it.
The website is http://www.tidlowhaulage.com.au/ and need:
1 x Front Page
1 x Location Page
Please keep the green colour scheme as this is the corporate colours but would like to steer away from the black.
Industry/Entity Type
It Company
Number of Pages Required
2 page
Font styles to use
Sans Serif
Requirements
Must have
- Clean & Professional
- Keep green colour scheme
Should not have
- Steer away from black
- not look like a template

```html
<!DOCTYPE html>
<html lang="en">
<head>
<meta charset="utf-8">
<title>Tidlow Haulage – Rubbish Removal</title>
<link href="https://fonts.googleapis.com/css2?family=Open+Sans:wght@400;600;700;800&display=swap" rel="stylesheet">
<style>
:root{
  --green:#5fb52a;
  --green-dark:#3f8f16;
  --green-light:#8fd44a;
  --text:#555c63;
  --heading:#3b4148;
  --muted:#9aa0a6;
  --line:#e2e4e6;
  --grey-bg:#f1f2f3;
  --white:#ffffff;
  --yellow:#f4c21b;
}
*{box-sizing:border-box;margin:0;padding:0}
html,body{width:1200px;height:3240px;overflow:hidden}
body{font-family:"Open Sans",Arial,sans-serif;color:var(--text);background:var(--white);position:relative}
a{color:inherit;text-decoration:none}
ul{list-style:none}

/* header */
.site-header{height:120px;display:flex;align-items:center;justify-content:space-between;padding:0 150px 0 120px}
.brand{display:flex;align-items:center;gap:14px;font-size:34px;font-weight:800;color:var(--green-dark);letter-spacing:-.5px}
.brand-mark{width:22px;height:22px;background:var(--green)}
.header-phone{border:2px solid var(--green);border-radius:6px;padding:10px 22px;font-size:20px;font-weight:600;color:var(--heading);display:flex;align-items:center;gap:10px}
.main-nav{height:48px;background:var(--green);display:flex;justify-content:center}
.main-nav ul{display:flex;gap:0}
.main-nav li{font-size:15px;font-weight:700;color:var(--white);padding:0 22px;line-height:48px;text-transform:uppercase}
.main-nav li.active{background:var(--green-dark)}

/* hero */
.hero{height:492px;position:relative;background:linear-gradient(135deg,#7e8a80 0%,#5d6d62 40%,#4c6256 70%,#8b8d7e 100%);display:flex;flex-direction:column;align-items:center;justify-content:center;color:var(--white);text-align:center}
.hero::before{content:"";position:absolute;inset:0;background:rgba(40,50,44,.35)}
.hero > *{position:relative}
.hero h1{font-size:52px;font-weight:800;letter-spacing:1px;text-transform:uppercase;margin-top:20px}
.hero p{font-size:34px;font-weight:600;letter-spacing:1px;text-transform:uppercase;margin-top:4px}
.btn{display:inline-block;background:var(--green);color:var(--white);font-weight:700;text-transform:uppercase;border-radius:4px}
.hero .btn{font-size:17px;padding:12px 30px;margin-top:22px}
.hero-dots{position:absolute;bottom:26px;display:flex;gap:10px}
.hero-dots span{width:12px;height:12px;border-radius:50%;background:rgba(255,255,255,.55)}
.hero-dots span.on{background:var(--white)}

/* services */
.services{height:460px;text-align:center;padding-top:58px}
.section-title{font-size:34px;font-weight:700;color:var(--heading);line-height:1.3}
.lead{font-size:14px;line-height:1.7;color:var(--muted);width:600px;margin:22px auto 0}
.service-list{display:flex;justify-content:center;gap:70px;margin-top:40px}
.service{display:flex;align-items:center;gap:18px}
.service-icon{width:96px;height:96px;border-radius:50%;border:2px solid var(--line);display:flex;align-items:center;justify-content:center}
.service h3{font-size:20px;font-weight:700;color:var(--green-dark);text-align:left;line-height:1.25}
.service h3 span{display:block;color:var(--green)}

/* enquiry */
.enquiry{height:460px;background:var(--grey-bg);position:relative;padding:90px 0 0 120px}
.eyebrow{font-size:22px;font-weight:600;color:var(--green)}
.enquiry h2{font-size:30px;font-weight:700;color:var(--heading);margin-top:4px;white-space:nowrap;position:relative;z-index:2}
.enquiry .copy{font-size:13px;line-height:1.75;color:var(--muted);width:310px;margin-top:14px}
.enquiry .btn{font-size:14px;padding:9px 22px;margin-top:18px;text-transform:none}
.skip-bin{position:absolute;left:540px;top:195px;width:200px;height:205px;background:linear-gradient(160deg,#ffd84a,#e4a911);border-radius:8px}
.enquiry-form{position:absolute;left:760px;top:60px;width:300px;background:var(--white);padding:18px 22px 24px;box-shadow:0 2px 10px rgba(0,0,0,.08)}
.enquiry-form h3{font-size:24px;font-weight:600;color:var(--heading);margin-bottom:14px}
.field{border:1px solid var(--line);height:36px;margin-bottom:12px;font-size:13px;color:var(--muted);display:flex;align-items:center;gap:8px;padding:0 10px}
.field .dot{width:10px;height:10px;background:var(--muted);border-radius:2px}
.field.message{height:70px;align-items:flex-start;padding-top:10px}
.enquiry-form .btn{width:100%;text-align:center;font-size:15px;padding:10px 0;background:linear-gradient(var(--green),var(--green-dark))}

/* why */
.why{height:540px;position:relative}
.worker-photo{position:absolute;left:120px;top:70px;width:380px;height:470px;background:linear-gradient(180deg,#eef0ec 0%,#c9b49a 50%,#8fc44f 100%)}
.why-body{position:absolute;left:540px;top:100px;width:540px}
.why h2{font-size:30px;font-weight:700;color:var(--green-dark)}
.why .copy{font-size:13px;line-height:1.75;color:var(--muted);margin-top:14px;width:480px}
.features{display:grid;grid-template-columns:1fr 1fr;gap:34px 30px;margin-top:34px}
.feature{display:flex;gap:14px;align-items:center}
.feature-icon{width:56px;height:56px;border-radius:50%;background:var(--green);display:flex;align-items:center;justify-content:center;flex:none}
.feature h4{font-size:20px;font-weight:700;color:var(--heading)}
.feature p{font-size:11px;color:var(--muted);margin-top:2px}

/* testimonials */
.testimonials{height:460px;background:radial-gradient(ellipse at 35% 40%,var(--green-light),var(--green) 55%,var(--green-dark));position:relative;color:var(--white)}
.testimonials h2{position:absolute;left:0;width:880px;text-align:center;top:70px;font-size:36px;font-weight:600}
.quote{position:absolute;left:200px;top:150px;width:480px;display:flex;gap:16px}
.quote-mark{font-size:70px;font-weight:800;line-height:.8}
.quote p{font-size:17px;line-height:1.65;font-style:italic}
.quote cite{display:block;font-style:normal;font-size:15px;font-weight:700;margin-top:24px}
.quote small{display:block;font-size:12px;opacity:.85}
.couple-photo{position:absolute;right:120px;bottom:0;width:340px;height:420px;background:linear-gradient(180deg,rgba(255,255,255,.25),#e8e4e0 60%,#d7d1cb)}

/* locations */
.locations{height:320px;padding:40px 120px 0}
.locations h2{font-size:30px;font-weight:600;color:var(--heading)}
.location-cols{display:grid;grid-template-columns:repeat(4,1fr);margin-top:26px;padding-left:20px}
.location-cols li{font-size:13px;color:var(--text);line-height:23px;display:flex;align-items:center;gap:8px}
.location-cols li::before{content:"";width:6px;height:6px;border-radius:50%;background:var(--green)}

/* footer */
.site-footer{height:300px;background:var(--grey-bg);border-top:1px solid var(--line);display:flex;padding:42px 120px 0;gap:90px}
.site-footer h3{font-size:24px;font-weight:600;color:var(--heading);margin-bottom:14px}
.quick-links{display:flex;gap:60px}
.quick-links li,.contact li{font-size:13px;line-height:22px;color:var(--text)}
.footer-col-links{width:380px}
.contact{width:320px}
.contact li{display:flex;gap:8px;align-items:center}
.contact .ico{width:10px;height:10px;background:var(--green);border-radius:50%;flex:none}
.social{display:flex;gap:8px}
.social span{width:30px;height:30px;border-radius:50%;background:var(--green)}
.cards{display:flex;gap:8px;margin-top:16px}
.cards span{width:44px;height:28px;border-radius:3px;background:#dcdfe2}
.bottom-bar{height:40px;display:flex;align-items:center;justify-content:center;font-size:12px;color:var(--muted);background:var(--white)}
</style>
</head>
<body>

<header class="site-header">
  <div class="brand"><span class="brand-mark"></span>Tidlow Haulage</div>
  <div class="header-phone">
    <svg width="18" height="18" viewBox="0 0 24 24"><path d="M6.6 10.8a15 15 0 006.6 6.6l2.2-2.2c.3-.3.7-.4 1-.2 1.1.4 2.3.6 3.6.6.6 0 1 .4 1 1V20c0 .6-.4 1-1 1A17 17 0 013 4c0-.6.4-1 1-1h3.5c.6 0 1 .4 1 1 0 1.3.2 2.5.6 3.6.1.3 0 .7-.2 1z" fill="#5fb52a"/></svg>
    (0400) 555 019
  </div>
</header>
<nav class="main-nav">
  <ul>
    <li class="active">Home</li><li>About Us</li><li>Services</li><li>Gallery</li><li>Blogs</li><li>Testimonial</li><li>FAQ</li><li>Location</li><li>Contact</li>
  </ul>
</nav>

<section class="hero" role="img" aria-label="Photo of a green skip bin loaded with rubbish beside a building site">
  <h1>Rubbish Removal Service</h1>
  <p>Mauris vel lacus vitae felis</p>
  <a class="btn">Free Quote Now</a>
  <div class="hero-dots"><span class="on"></span><span></span><span></span><span></span></div>
</section>

<section class="services">
  <h2 class="section-title">Sydney's Cheapest Rubbish<br>Removal Services</h2>
  <p class="lead">Our team of professional and friendly rubbish removalists in Sydney take real pride in their work. We're a local company who understands what the Sydney locals want, fast and tidy collection plus honest pricing, clean ups and junk removal, we get the job done.</p>
  <div class="service-list">
    <div class="service">
      <div class="service-icon"><svg width="48" height="48" viewBox="0 0 48 48" fill="none" stroke="#5fb52a" stroke-width="2.5"><path d="M6 24L24 9l18 15"/><path d="M11 20v19h26V20"/><path d="M20 39V28h8v11"/></svg></div>
      <h3>House Rubbish <span>Removals</span></h3>
    </div>
    <div class="service">
      <div class="service-icon"><svg width="48" height="48" viewBox="0 0 48 48" fill="none" stroke="#5fb52a" stroke-width="2.5"><rect x="10" y="7" width="20" height="34"/><rect x="30" y="18" width="10" height="23"/><path d="M15 13h4M22 13h3M15 20h4M22 20h3M15 27h4M22 27h3M6 41h38"/></svg></div>
      <h3>Office Rubbish <span>Removals</span></h3>
    </div>
    <div class="service">
      <div class="service-icon"><svg width="48" height="48" viewBox="0 0 48 48" fill="none" stroke="#5fb52a" stroke-width="2.5"><path d="M6 18h26l-4 14H12z"/><circle cx="34" cy="36" r="4"/><path d="M28 32l6 4M32 18l8-6"/></svg></div>
      <h3>Construction Rubbish <span>Removals</span></h3>
    </div>
  </div>
</section>

<section class="enquiry">
  <p class="eyebrow">Enquiry Now &amp; Recieve a Call back</p>
  <h2>Best Price Rubbish Removal</h2>
  <p class="copy">Tidlow Haulage offers some of the best prices in Sydney. We provide an exceptional, friendly and affordable same day rubbish service for all volumes of rubbish. Our team of experience and on time rubbish removalists can remove or dispose of household rubbish, garden rubbish, office goods and unwanted household furniture.</p>
  <a class="btn">Learn More</a>
  <div class="skip-bin" role="img" aria-label="Illustration of a yellow skip bin"></div>
  <form class="enquiry-form">
    <h3>Get an Enquiry Now</h3>
    <div class="field"><span class="dot"></span>Name</div>
    <div class="field"><span class="dot"></span>Email</div>
    <div class="field"><span class="dot"></span>Phone</div>
    <div class="field message">Message</div>
    <a class="btn">Submit</a>
  </form>
</section>

<section class="why">
  <div class="worker-photo" role="img" aria-label="Photo of a worker in a hard hat carrying timber offcuts in a green recycling crate"></div>
  <div class="why-body">
    <h2>Why Choose Us</h2>
    <p class="copy">Tidlow Haulage offers complete rubbish removal services for your home or business including residential household, office, retail business, building sites, demolition and more. We are a trusted Sydney rubbish removal company.</p>
    <div class="features">
      <div class="feature">
        <div class="feature-icon"><svg width="26" height="26" viewBox="0 0 24 24" fill="none" stroke="#fff" stroke-width="2"><path d="M3 12l9-9h8v8l-9 9z"/><circle cx="16" cy="8" r="1.5"/></svg></div>
        <div><h4>Cheapest Price</h4><p>Fair rates at every job we do</p></div>
      </div>
      <div class="feature">
        <div class="feature-icon"><svg width="26" height="26" viewBox="0 0 24 24" fill="none" stroke="#fff" stroke-width="2"><rect x="3" y="5" width="18" height="16"/><path d="M3 10h18M8 3v4M16 3v4"/></svg></div>
        <div><h4>Same Day</h4><p>Booked now, cleared the same day</p></div>
      </div>
      <div class="feature">
        <div class="feature-icon"><svg width="26" height="26" viewBox="0 0 24 24" fill="none" stroke="#fff" stroke-width="2"><circle cx="12" cy="12" r="9"/><path d="M12 7v5l3 3"/></svg></div>
        <div><h4>Always on Time</h4><p>We arrive when we say we will</p></div>
      </div>
      <div class="feature">
        <div class="feature-icon"><svg width="26" height="26" viewBox="0 0 24 24" fill="none" stroke="#fff" stroke-width="2"><path d="M5 12l5 5 9-10"/></svg></div>
        <div><h4>10+ Year Exp</h4><p>A decade of local junk removal</p></div>
      </div>
    </div>
  </div>
</section>

<section class="testimonials">
  <h2>Testimonials</h2>
  <blockquote class="quote">
    <span class="quote-mark">&ldquo;</span>
    <div>
      <p>Friendly team who turned up right on time, cleared the whole garage in an hour and left the driveway spotless. Fair price too, I will happily book them again.</p>
      <cite>By Author Name<small>City Location</small></cite>
    </div>
  </blockquote>
  <div class="couple-photo" role="img" aria-label="Photo of a smiling couple, happy customers"></div>
</section>

<section class="locations">
  <h2>Our Location</h2>
  <div class="location-cols">
    <ul><li>Alexandria</li><li>Baulkham Hills</li><li>Bellevue Hill</li><li>Bondi</li><li>Bondi Junction</li><li>Chatswood</li></ul>
    <ul><li>Double Bay</li><li>Dover Heights</li><li>Kensington</li><li>Kingsford</li><li>Matraville</li><li>Marrickville</li></ul>
    <ul><li>Maroubra</li><li>Mascot</li><li>Malabar</li><li>Paddington</li><li>Potts Point</li><li>Randwick</li></ul>
    <ul><li>Rose Bay</li><li>St Peters</li><li>Surry Hills</li><li>Sydney CBD</li><li>Vaucluse</li><li>Waverley</li></ul>
  </div>
</section>

<footer class="site-footer">
  <div class="footer-col-links">
    <h3>Quick Links</h3>
    <div class="quick-links">
      <ul><li>Home</li><li>About us</li><li>Our Services</li><li>Why Us</li><li>Gallery</li></ul>
      <ul><li>FAQ</li><li>Testimonial</li><li>Locations</li><li>Blogs</li><li>Contact us</li></ul>
    </div>
  </div>
  <div class="contact">
    <h3>Contact Us</h3>
    <ul>
      <li><span class="ico"></span>12 Harbour Lane, Unit 4<br>Sydney NSW 2000</li>
      <li><span class="ico"></span>(0400) 555 020</li>
      <li><span class="ico"></span>info@tidlowhaulage.com.au</li>
    </ul>
  </div>
  <div class="follow">
    <h3>Follow Us</h3>
    <div class="social"><span></span><span></span><span></span><span></span><span></span></div>
    <div class="cards"><span></span><span></span><span></span><span></span></div>
  </div>
</footer>
<div class="bottom-bar">© 2016 Tidlow Haulage. All rights reserved. Term of Use</div>

</body>
</html>
```